Small Firewood bag design (for use it retail stores NZ)

Hi, we are a small business in New Zealand selling firewood. We have started to bag our wood and are now selling to stores in NZ. We are in need of a good firewood bag design. The overall size to be 40cm high x 25cm wide, however the text should be at minimum 2cm within this, as to prevent it from going around the corner of the bag.
We will only be printing the label on 1 side of the bag, and would like a design for black printing only and a design with black and orange/flame color.
Our business is called 'Kettle Ridge Firewood', (KRF Limited)
The product/wood type is Black Wattle.
The wood is a very hardwood, makes a great burner, burns hot and long, especially when compared to pine.
Our firewood is naturally seasoned outside in the northland sun.
Black wattle is of the Acacia family from Australia.
The bags are only small, 12kg or 25 litres.
It will be printed onto clear woven PP bags, see image. So intricate drawings is not recommended.
There will be no barcode on the label, as this will be sewn onto the bag separately.
Can provide our contact details for the bag later.

Note, the below images I designed on an online AI program, but do quite like the look of them.

Target Market(s)

Will be for sale in large department stores, petrol stations, some liquor stores and some dairy's. Target market is older people, people going to the batch, wood for people not organized to get in bulk amounts of wood

Industry/Entity Type

Firewood, home heating, winter, cold

Colors

Designer to choose colors to be used in the design.

Requirements
Nice to have
• Possibly an image of logs with the flames around it

```html
<!DOCTYPE html>
<html lang="en">
<head>
<meta charset="utf-8">
<title>Kettle Ridge Firewood – Bag Label</title>
<link rel="stylesheet" href="https://fonts.googleapis.com/css2?family=Anton&family=Oswald:wght@500;600;700&family=Montserrat:wght@600;700&display=swap">
<style>
  :root {
    --ink: #111111;
    --flame: #f26a21;
    --paper: #ffffff;
    --backdrop: #ffffff;
    --bag-edge: #2a2a2a;
  }
  html, body {
    margin: 0;
    padding: 0;
    width: 1200px;
    height: 1200px;
    overflow: hidden;
    background: var(--backdrop);
  }
  .bag {
    position: absolute;
    left: 256px;
    top: 50px;
    width: 687px;
    height: 1100px;
    box-sizing: border-box;
    border: 1px solid var(--bag-edge);
    background: var(--paper);
  }
  .label-frame {
    position: absolute;
    left: 54px;
    top: 54px;
    width: 578px;
    height: 992px;
    box-sizing: border-box;
    border: 17px solid var(--ink);
  }
  .label-art {
    position: absolute;
    left: -17px;
    top: -17px;
    width: 578px;
    height: 992px;
    overflow: hidden;
  }
  .uses-intro, .brand-banner, .contact, .company, .address {
    font-family: "Montserrat", sans-serif;
  }
  .uses, .weight, .features {
    font-family: "Oswald", sans-serif;
  }
  .title {
    font-family: "Anton", sans-serif;
  }
</style>
</head>
<body>
  <div class="bag">
    <div class="label-frame">
      <svg class="label-art" viewBox="0 0 578 992" xmlns="http://www.w3.org/2000/svg">
        <defs>
          <linearGradient id="fireGlow" x1="0" y1="0" x2="0" y2="1">
            <stop offset="0" stop-color="#f26a21"/>
            <stop offset="0.55" stop-color="#f4a06a"/>
            <stop offset="1" stop-color="#3a3a3a"/>
          </linearGradient>
        </defs>

        <!-- Uses list -->
        <text class="uses-intro" x="42" y="62" font-size="16" font-weight="600" fill="var(--ink)" textLength="140" lengthAdjust="spacingAndGlyphs">Great Choice for</text>
        <line x1="42" y1="67" x2="186" y2="67" stroke="var(--ink)" stroke-width="1.5"/>
        <text class="uses" x="42" y="106" font-size="42" font-weight="600" fill="var(--ink)" textLength="142" lengthAdjust="spacingAndGlyphs">BARBEQUES</text>
        <line x1="42" y1="113" x2="200" y2="113" stroke="var(--ink)" stroke-width="1.5"/>
        <text class="uses" x="42" y="151" font-size="42" font-weight="600" fill="var(--ink)" textLength="156" lengthAdjust="spacingAndGlyphs">PIZZA OVENS</text>
        <line x1="42" y1="158" x2="200" y2="158" stroke="var(--ink)" stroke-width="1.5"/>
        <text class="uses" x="42" y="196" font-size="42" font-weight="600" fill="var(--ink)" textLength="106" lengthAdjust="spacingAndGlyphs">&amp; BRAAI</text>
        <line x1="42" y1="203" x2="165" y2="203" stroke="var(--ink)" stroke-width="1.5"/>

        <!-- Campfire artwork area -->
        <rect class="campfire-art" x="214" y="52" width="176" height="200" rx="6" fill="url(#fireGlow)" role="img" aria-label="Illustration of stacked firewood logs with orange flames rising above them"/>

        <!-- Weight -->
        <text class="weight" x="448" y="82" font-size="40" font-weight="700" fill="var(--ink)" textLength="74" lengthAdjust="spacingAndGlyphs">12 kg</text>

        <!-- Wood type banner -->
        <rect x="164" y="283" width="250" height="31" fill="var(--ink)"/>
        <text class="brand-banner" x="289" y="308" font-size="26" font-weight="700" fill="var(--paper)" text-anchor="middle" textLength="232" lengthAdjust="spacingAndGlyphs">BLACK WATTLE</text>

        <!-- Product title -->
        <text class="title" x="288" y="461" font-size="159" fill="var(--ink)" text-anchor="middle" textLength="404" lengthAdjust="spacingAndGlyphs">KETTLE</text>
        <text class="title" x="288" y="616" font-size="158" fill="var(--flame)" text-anchor="middle" textLength="290" lengthAdjust="spacingAndGlyphs">RIDGE</text>
        <text class="title" x="288" y="772" font-size="159" fill="var(--flame)" text-anchor="middle" textLength="471" lengthAdjust="spacingAndGlyphs">FIREWOOD</text>

        <!-- Features -->
        <text class="features" x="55" y="816" font-size="32" font-weight="500" fill="var(--ink)" textLength="216" lengthAdjust="spacingAndGlyphs">QUALITY HARDWOOD</text>
        <line x1="281" y1="791" x2="281" y2="814" stroke="var(--ink)" stroke-width="2.5"/>
        <text class="features" x="294" y="816" font-size="32" font-weight="500" fill="var(--ink)" textLength="225" lengthAdjust="spacingAndGlyphs">LONG BURN DURATION</text>
        <text class="features" x="76" y="853" font-size="32" font-weight="500" fill="var(--ink)" textLength="192" lengthAdjust="spacingAndGlyphs">HIGH HEAT OUTPUT</text>
        <line x1="284" y1="828" x2="284" y2="851" stroke="var(--ink)" stroke-width="2.5"/>
        <text class="features" x="304" y="853" font-size="32" font-weight="500" fill="var(--ink)" textLength="195" lengthAdjust="spacingAndGlyphs">LOW ASH CONTENT</text>

        <!-- Company -->
        <text class="company" x="289" y="915" font-size="24" font-weight="700" fill="var(--ink)" text-anchor="middle" textLength="170" lengthAdjust="spacingAndGlyphs">KRF LIMITED</text>

        <!-- Address -->
        <g class="icon-pin" transform="translate(79 925)">
          <path d="M6 0 C2.7 0 0 2.6 0 5.9 C0 10 6 16 6 16 C6 16 12 10 12 5.9 C12 2.6 9.3 0 6 0 Z" fill="var(--ink)"/>
          <circle cx="6" cy="6" r="2.4" fill="var(--paper)"/>
        </g>
        <text class="address" x="96" y="940" font-size="18" font-weight="600" fill="var(--ink)" textLength="402" lengthAdjust="spacingAndGlyphs">Lorem Ipsum, Lorem Ipsum, NewZeland.</text>

        <!-- Contact line -->
        <g class="icon-phone" transform="translate(50 950)">
          <circle cx="8" cy="8" r="7.5" fill="none" stroke="var(--ink)" stroke-width="1.5"/>
          <path d="M5 4.5 L6.8 4.5 L7.4 6.6 L6.4 7.4 C6.9 8.6 7.6 9.3 8.7 9.8 L9.5 8.8 L11.6 9.4 L11.6 11.2 C8 11.4 4.8 8.2 5 4.5 Z" fill="var(--ink)"/>
        </g>
        <text class="contact" x="73" y="965" font-size="18" font-weight="700" fill="var(--ink)" textLength="110" lengthAdjust="spacingAndGlyphs">990048217</text>
        <g class="icon-mail" transform="translate(192 953)">
          <rect x="0" y="0" width="16" height="12" fill="var(--ink)"/>
          <path d="M1 1 L8 7 L15 1" fill="none" stroke="var(--paper)" stroke-width="1.4"/>
        </g>
        <text class="contact" x="214" y="965" font-size="18" font-weight="700" fill="var(--ink)" textLength="138" lengthAdjust="spacingAndGlyphs">info@krfl.com</text>
        <g class="icon-globe" transform="translate(362 950)" fill="none" stroke="var(--ink)" stroke-width="1.4">
          <circle cx="8" cy="8" r="7.3"/>
          <ellipse cx="8" cy="8" rx="3.3" ry="7.3"/>
          <line x1="0.7" y1="8" x2="15.3" y2="8"/>
          <line x1="2" y1="4.2" x2="14" y2="4.2"/>
          <line x1="2" y1="11.8" x2="14" y2="11.8"/>
        </g>
        <text class="contact" x="385" y="965" font-size="18" font-weight="700" fill="var(--ink)" textLength="140" lengthAdjust="spacingAndGlyphs">www.krfl.com</text>
      </svg>
    </div>
  </div>
</body>
</html>
```